Documentary Movie Needs a Poster

We need a poster/lobby card for a documentary film made by six filmmakers. Lobby card needs to list name of sponsor, names of filmmakers and (if feasible, but not required) image frames from each of the six sections of the film.

Text should be very readable. OK to have all caps text or upper/lower.

Design comps are OK, these do not need to be print-ready final images.

Target Market(s)

well educated documentary filmgoers

Industry/Entity Type

Movie

Requirements
Must have
• Must contain the following text (please use helvetica neue or similar font).

Please use the following sponsor name:

The
Marlowe Institute for Cinema
presents

Please use the following filmmaker names:

Theodore Pelusky
Robert Nash
Frederick Tamworth
Harold E. F. Pratt
Vincent Lorimer
Danny Frost

Please use the 6 images in archive/zip to create the card.

You can also do text-only versions of the card (no images).

Card needs to be 2:1 aspect ratio (2000px wide x 1000 pixels high)

Names of filmmakers should each be same size (no filmmaker has visual priority over the other).

Colors for text, lines and other design elements should be RED, BLACK and/or WHITE.

Feel free to crop images if you need to.

```html
<!DOCTYPE html>
<html lang="en">
<head>
<meta charset="utf-8">
<title>Marlowe Institute for Cinema presents</title>
<link rel="stylesheet" href="https://fonts.googleapis.com/css2?family=Archivo:wght@400;800&display=swap">
<style>
  :root {
    --ink: #0b0b0b;
    --white: #ffffff;
    --red: #d3151b;
    --frame: #1a1a1a;
    --shade: rgba(12, 12, 12, 0.55);
  }
  * { margin: 0; padding: 0; box-sizing: border-box; }
  html, body { width: 1200px; height: 600px; overflow: hidden; background: var(--ink); }
  .card {
    position: relative;
    width: 1200px;
    height: 600px;
    overflow: hidden;
    background: var(--frame);
    font-family: "Archivo", "Helvetica Neue", Arial, sans-serif;
  }
  .film-frames {
    position: absolute;
    inset: 0;
    display: grid;
    grid-template-columns: 402px 394px 1fr;
    grid-template-rows: 290px 1fr;
    gap: 4px;
  }
  .frame { width: 100%; height: 100%; }
  .frame--soldier-ruins { background: linear-gradient(160deg, #8a8a84 0%, #5b5b57 55%, #3d3d3a 100%); }
  .frame--capitol-protest { background: linear-gradient(180deg, #6c7f96 0%, #9aa3a8 45%, #5c5a52 100%); }
  .frame--wrecked-vehicle { background: linear-gradient(200deg, #b8a98d 0%, #8e7c60 50%, #5e5240 100%); }
  .frame--rooftop-patrol { background: linear-gradient(170deg, #9a9478 0%, #6d6a52 50%, #3f3d2f 100%); }
  .frame--armed-crowd { background: linear-gradient(180deg, #8c7660 0%, #5e4a38 55%, #3a2c22 100%); }
  .frame--checkpoint { background: linear-gradient(190deg, #a9a294 0%, #7d7768 50%, #4e4a40 100%); }

  .vignette {
    position: absolute;
    inset: 0;
    background: radial-gradient(ellipse at center, rgba(0,0,0,0) 40%, rgba(0,0,0,0.55) 100%);
  }
  .name-band {
    position: absolute;
    left: 0; right: 0;
    top: 160px;
    height: 400px;
    background: var(--shade);
  }

  .presenter {
    position: absolute;
    left: 0; right: 0;
    top: 44px;
    text-align: center;
    color: var(--white);
    text-shadow: 0 1px 4px rgba(0,0,0,0.5);
  }
  .presenter__article,
  .presenter__verb {
    display: block;
    font-weight: 400;
    font-size: 27px;
    line-height: 1;
  }
  .presenter__sponsor-row {
    display: flex;
    align-items: center;
    justify-content: center;
    gap: 14px;
    height: 36px;
    margin: 8px 0 6px;
  }
  .presenter__marker {
    width: 14px;
    height: 14px;
    background: var(--red);
  }
  .presenter__sponsor {
    color: var(--white);
    font-weight: 800;
    font-size: 27px;
    line-height: 36px;
    letter-spacing: 0.09em;
    text-transform: uppercase;
    white-space: nowrap;
  }

  .filmmakers {
    position: absolute;
    left: 0; right: 0;
    top: 170px;
    list-style: none;
    text-align: center;
  }
  .filmmakers__name {
    color: var(--white);
    font-weight: 800;
    font-size: 56px;
    line-height: 64px;
    letter-spacing: 0.1em;
    text-transform: uppercase;
    white-space: nowrap;
    text-shadow: 0 2px 6px rgba(0,0,0,0.6);
  }
</style>
</head>
<body>
<main class="card">
  <div class="film-frames">
    <div class="frame frame--soldier-ruins" role="img" aria-label="Black and white photo of a helmeted soldier resting among battlefield rubble"></div>
    <div class="frame frame--capitol-protest" role="img" aria-label="Protesters holding anti-war signs in front of a capitol dome"></div>
    <div class="frame frame--wrecked-vehicle" role="img" aria-label="Wrecked military vehicle lying in desert sand"></div>
    <div class="frame frame--rooftop-patrol" role="img" aria-label="Soldiers aiming rifles from a rooftop over a desert city"></div>
    <div class="frame frame--armed-crowd" role="img" aria-label="Crowd of men raising rifles in the air"></div>
    <div class="frame frame--checkpoint" role="img" aria-label="Soldier kneeling with a rifle on a road checkpoint"></div>
  </div>
  <div class="vignette"></div>
  <div class="name-band"></div>

  <header class="presenter">
    <span class="presenter__article">the</span>
    <div class="presenter__sponsor-row">
      <span class="presenter__marker" aria-hidden="true"></span>
      <span class="presenter__sponsor">Marlowe Institute for Cinema</span>
    </div>
    <span class="presenter__verb">presents</span>
  </header>

  <ul class="filmmakers">
    <li class="filmmakers__name">Theodore Pelusky</li>
    <li class="filmmakers__name">Robert Nash</li>
    <li class="filmmakers__name">Frederick Tamworth</li>
    <li class="filmmakers__name">Harold E. F. Pratt</li>
    <li class="filmmakers__name">Vincent Lorimer</li>
    <li class="filmmakers__name">Danny Frost</li>
  </ul>
</main>
</body>
</html>
```